Magnet for side of van (Al or eps)

I have some old files on my computer, so I created an image to make this project easier. The company making the magnet is requesting vector files. Specifically Al or eps. The size of the magnet that will fit on the van is approx. 30" x 10". I would like the design to work on any size magnet that can be ordered, but definitely close to the size provided. The magnet will be placed on a dark grey van so the background needs to be light color, white is fine. Not sure if they are cutting this out with a cutter, so if the graphics have to be lighter, then so be it. I'll update designers with that status soon. If you can keep the shades and the colors that would be nice, making solid colors would be fine too. Any new graphics would be nice, but not necessary. Fonts of the phone number and website can be changed if needed. Location of logo, name, number, or website address can be moved around if necessary. If you can add "Quality You Deserve", that would be nice, but not necessary. Letters BRM IS NOT necessary for this project. Just sending you the al and eps file if it helps for creation. I would like the colors be the same or close. Any questions, feel free to ask, if you need more ideas or details.
Industry/Entity Type
Computer
Requirements
Must have
- Company logo and name, telephone number and website.

```html
<!DOCTYPE html>
<html lang="en">
<head>
<meta charset="utf-8">
<title>Bright Ridge Mirror Glass – Van Magnet</title>
<link rel="stylesheet" href="https://fonts.googleapis.com/css2?family=Saira:wght@600&family=Source+Sans+3:wght@400;700&display=swap">
<style>
  :root {
    --bg-light: #ffffff;
    --bg-soft: #f1f2f3;
    --name-top: #85898d;
    --name-bottom: #53575b;
    --rule-grey: #85898d;
    --contact-dark: #3c3f42;
    --mark-fill: #c4c8cc;
  }
  * { margin: 0; padding: 0; box-sizing: border-box; }
  html, body {
    width: 1200px;
    height: 400px;
    overflow: hidden;
    background: var(--bg-light);
  }
  .magnet {
    position: relative;
    width: 1200px;
    height: 400px;
    overflow: hidden;
    background: radial-gradient(ellipse at 45% 40%, var(--bg-light) 0%, var(--bg-soft) 100%);
  }
  .brand-mark {
    position: absolute;
    left: 80px;
    top: 100px;
    width: 200px;
    height: 200px;
    background: var(--mark-fill);
  }
  .brand-name {
    position: absolute;
    left: 348px;
    top: 96px;
    width: 812px;
    height: 152px;
  }
  .brand-name text {
    font-family: "Saira", "Arial Narrow", sans-serif;
    font-weight: 600;
  }
  .brand-name__top { fill: var(--name-top); }
  .brand-name__bottom { fill: var(--name-bottom); }
  .brand-name__rule {
    stroke: var(--rule-grey);
    stroke-width: 2.5;
  }
  .contact {
    position: absolute;
    left: 346px;
    top: 276px;
    display: flex;
    align-items: center;
    font-family: "Source Sans 3", "Helvetica Neue", Arial, sans-serif;
    font-size: 32px;
    color: var(--contact-dark);
    line-height: 1;
  }
  .contact__phone { font-weight: 700; }
  .contact__divider {
    display: inline-block;
    width: 1.5px;
    height: 34px;
    margin: 0 11px;
    background: var(--contact-dark);
  }
  .contact__web { font-weight: 400; }
</style>
</head>
<body>
  <main class="magnet">
    <div class="brand-mark" aria-hidden="true"></div>

    <svg class="brand-name" viewBox="0 0 812 152" aria-label="Bright Ridge Mirror Glass">
      <text class="brand-name__top" x="2" y="56" font-size="70" textLength="802" lengthAdjust="spacing">BRIGHT RIDGE</text>
      <line class="brand-name__rule" x1="2" y1="72" x2="810" y2="72"/>
      <text class="brand-name__bottom" x="0" y="148" font-size="82" textLength="802" lengthAdjust="spacingAndGlyphs">MIRROR GLASS</text>
    </svg>

    <p class="contact">
      <span class="contact__phone">414-555-019</span>
      <span class="contact__divider"></span>
      <span class="contact__web">www.brmglass.com</span>
    </p>
  </main>
</body>
</html>
```